Modern Homepage Design for brenvik.nl – Fish & Chicken Food Webshop

Brenvik.nl is an online store that sells fish and chicken food. The design should be visually appealing, easy to navigate, and optimized for e-commerce. We want a layout that helps customers quickly find what they need and encourages them to explore our products.
A good example of the style and structure we like is dierkamp.nl – clean layout, clear product focus, and user-friendly navigation.
Brand Colors (must be used):
Orange: #f7a441
Dark Gray: #3c3c3b
White: #ffffff
Please use these colors consistently throughout the design.
Homepage Requirements:
The homepage should include the following sections:
Main Slider / Hero Banner
A large, eye-catching slider at the top of the page to highlight promotions or featured categories.
Category Blocks
A section with clear, clickable blocks or tiles that link to main product categories (e.g., Fish Food, Chicken Food, Accessories).
Featured Products
A section showcasing selected or best-selling products.
Special Offers / Promotions
A space to highlight current deals or limited-time offers.
Three Banners in a Row
A section with three horizontal banners side by side, which can be used for promotions, shipping info, or other key messages.
Unique Selling Points (USPs)
A section that briefly explains what makes our store different (e.g., fast delivery, high-quality feed, trusted by professionals).
SEO Content Block
A short paragraph of text for SEO purposes (use Lorem Ipsum for dummy content).
Footer Design
Include space for contact information, navigation links, and social media.
Design Notes:
The design must be responsive and mobile-friendly.
Focus on clean layout, good spacing, and easy navigation.
Use modern fonts and a clear visual hierarchy.
We are only looking for the homepage design at this stage, but we may work with the selected designer on additional pages later.
Deliverables:
Homepage design in layered PSD, Figma, or Adobe XD format
Any fonts and assets used
Preview images/mockups
We look forward to seeing your ideas and working with a designer who can bring our brand to life with a fresh and functional homepage design.
Let us know if you have any questions.
Hobby Animal Keepers, Pet Owners
Animal Nutrition & Feed
2 page

```html
<!DOCTYPE html>
<html lang="en">
<head>
<meta charset="utf-8">
<title>Brenvik.nl – Fish & Chicken Food</title>
<link href="https://fonts.googleapis.com/css2?family=Archivo:wght@400;500;600;700;800&display=swap" rel="stylesheet">
<style>
:root{
  --orange:#f7a441;
  --orange-deep:#f08f1c;
  --dark:#3c3c3b;
  --white:#ffffff;
  --light:#f3f3f3;
  --line:#e2e2e2;
  --text:#3c3c3b;
  --muted:#6b6b6b;
}
*{box-sizing:border-box;margin:0;padding:0}
html,body{width:1200px;height:3868px;overflow:hidden}
body{position:relative;background:var(--white);font-family:'Archivo',sans-serif;color:var(--text)}
.abs{position:absolute}
a{color:inherit;text-decoration:none}

/* top bar */
.topbar{left:0;top:0;width:1200px;height:42px;font-size:11px;display:flex;align-items:center;justify-content:space-between;padding:0 90px 0 105px}
.topbar span{display:inline-flex;align-items:center;gap:5px;margin-right:12px}
/* header */
.header{left:0;top:42px;width:1200px;height:93px;background:linear-gradient(90deg,var(--orange) 0%,#fbc78a 40%,var(--orange) 100%)}
.logo{left:92px;top:22px;color:var(--white);font-weight:800;font-size:38px;line-height:48px;letter-spacing:-0.5px}
.search{left:380px;top:23px;width:570px;height:48px;border-radius:24px;background:var(--white);border:2px solid var(--dark);display:flex;align-items:center;justify-content:space-between;padding:0 4px 0 28px;font-size:11px;color:#999}
.search b{background:var(--dark);color:var(--white);border-radius:20px;height:36px;width:146px;display:flex;align-items:center;justify-content:center;font-weight:600;font-size:12px;gap:6px}
.hbtn{top:23px;width:48px;height:48px;border-radius:50%;background:var(--white);border:2px solid var(--dark);display:flex;align-items:center;justify-content:center}
.nav{left:0;top:135px;width:1200px;height:45px;background:var(--dark);display:flex;justify-content:center;align-items:center}
.nav a{color:var(--white);font-size:14px;font-weight:600;margin:0 22px}

/* hero */
.hero-main{left:65px;top:245px;width:743px;height:393px;border-radius:34px;overflow:hidden;background:linear-gradient(100deg,#c8661c 0%,#f39a2e 35%,#fbb450 70%,#f59c2c 100%)}
.hero-photo{left:0;top:0;width:330px;height:393px;background:radial-gradient(ellipse at 40% 40%,#b3432a 0%,#7c3b22 40%,rgba(230,130,40,0) 75%)}
.hero-title{left:317px;top:130px;font-size:33px;font-weight:800;line-height:36px;color:var(--white)}
.hero-title em{font-style:normal;color:var(--dark)}
.hero-sub{left:318px;top:217px;font-size:13px;line-height:20px;color:var(--white);width:290px}
.hero-cta{left:488px;top:252px;width:86px;height:76px;border-radius:50%;background:var(--dark);border:3px solid var(--white);color:var(--white);font-size:10px;font-weight:700;display:flex;align-items:center;justify-content:center;text-align:center;line-height:11px;transform:rotate(20deg)}
.hero-side{left:823px;top:245px;width:312px;height:393px;border-radius:34px;overflow:hidden;background:radial-gradient(circle at 60% 55%,#e6a45a 0%,#3f8db0 28%,#125e86 60%,#0a3550 100%)}
.hero-side h2{position:absolute;top:56px;left:0;width:100%;text-align:center;color:var(--white);font-size:23px;font-weight:800;line-height:28px}

.h-center{left:0;width:1200px;text-align:center;font-size:29px;font-weight:700}
.divider{left:65px;width:1070px;height:1px;background:var(--line)}

/* categories */
.cat-tile{top:850px;width:195px;height:101px;border-radius:18px}
.cat-pack{top:783px;border-radius:8px}
.cat-label{top:967px;width:195px;text-align:center;font-size:16px;font-weight:600}

/* favorites */
.fav-title{left:105px;top:1110px;font-size:31px;font-weight:700}
.fav-desc{left:106px;top:1160px;width:520px;font-size:11px;line-height:17px;color:#555}
.arrow{top:1130px;width:52px;height:52px;border-radius:50%;display:flex;align-items:center;justify-content:center}
.card{top:1223px;width:234px;height:307px;border-radius:18px;background:var(--light);border:1.5px solid #dcdcdc}
.card .img{position:absolute;left:10px;top:10px;width:212px;height:140px;border-radius:14px;background:var(--white)}
.card .pack{position:absolute;left:76px;top:20px;width:60px;height:100px;border-radius:6px}
.card .stars{position:absolute;left:32px;top:174px;color:var(--orange);font-size:12px;letter-spacing:1px}
.card .name{position:absolute;left:32px;top:202px;font-size:16px;line-height:22px;font-weight:500}
.card .price{position:absolute;left:32px;top:254px;font-size:24px;font-weight:700;color:var(--orange);display:flex;align-items:baseline;gap:6px}
.card .price small{font-size:8px;color:var(--dark);font-weight:500}
.card .cart{position:absolute;left:173px;top:238px;width:38px;height:38px;border-radius:50%;background:var(--orange);display:flex;align-items:center;justify-content:center}
.promo{left:107px;top:1547px;width:985px;height:59px;border-radius:14px;background:linear-gradient(90deg,#f9b15e,#f7a441 50%,#f59632);display:flex;align-items:center;color:var(--white)}
.promo p{position:absolute;left:282px;font-size:17px;font-weight:500}
.promo a{position:absolute;left:823px;font-size:13px;text-decoration:underline;font-weight:600}
.promo i{position:absolute;left:908px;width:22px;height:20px;background:var(--white);border-radius:4px;display:flex;align-items:center;justify-content:center}

/* deals */
.deals-title{left:113px;top:1750px;font-size:31px;font-weight:700}
.pill{height:36px;border-radius:18px;background:#e5e5e5;display:flex;align-items:center;justify-content:center;font-size:12px;font-weight:600}
.deal{border-radius:18px;overflow:hidden;box-shadow:0 14px 30px rgba(0,0,0,.12)}
.deal h3{position:absolute;color:var(--white);font-size:21px;line-height:27px;font-weight:800}

/* features */
.feat{top:2260px;display:flex;align-items:center;gap:18px}
.feat .ic{width:60px;height:60px;border-radius:10px;display:flex;align-items:center;justify-content:center}
.feat b{display:block;font-size:19px;font-weight:600}
.feat small{display:block;font-size:11px;margin-top:8px;font-weight:500;color:#444}

/* why */
.why{top:2545px;width:150px;text-align:center}
.why .circle{width:124px;height:124px;margin:0 auto;border-radius:50%;background:var(--orange);display:flex;align-items:center;justify-content:center}
.why p{margin-top:33px;font-size:13px;line-height:17px;color:#444}

/* partner */
.partner-img{left:210px;top:2873px;width:352px;height:402px;background:linear-gradient(150deg,#b44835 0%,#6c5a4a 35%,#3e6aa8 60%,#8a7a66 100%);border-radius:52% 48% 44% 56% / 38% 46% 54% 62%}
.partner h2{left:635px;top:2930px;font-size:31px;line-height:36px;font-weight:700}
.partner p{left:636px;top:3022px;width:360px;font-size:12px;line-height:19.5px;color:#333}

/* footer */
.footer{left:0;top:3402px;width:1200px;height:466px;background:var(--dark);border-radius:90px 90px 0 0;color:var(--white)}
.fcol{top:120px}
.fcol h4{color:var(--orange);font-size:19px;font-weight:700;margin-bottom:28px}
.fcol li{list-style:none;font-size:15px;margin-bottom:15px;display:flex;gap:8px}
.fcol li::before{content:"›";color:var(--orange)}
.fcol.contact li::before{content:none}
.fsep{top:125px;width:1px;height:150px;background:#5a5a59}
.social{top:406px;width:32px;height:32px;border-radius:50%;background:#555554}
.fbottom{top:414px;font-size:11px}
.totop{left:1130px;top:358px;width:40px;height:40px;border-radius:50%;background:var(--orange);display:flex;align-items:center;justify-content:center}
</style>
</head>
<body>

<div class="abs topbar">
  <div>
    <span><svg width="11" height="9" viewBox="0 0 11 9"><rect width="11" height="9" rx="1" fill="#f7a441"/><path d="M0 1l5.5 4L11 1" stroke="#fff" fill="none"/></svg>info@brenvik.nl</span>
    <span><svg width="10" height="10" viewBox="0 0 10 10"><path d="M2 0l2 2-1 2 3 3 2-1 2 2-2 2C4 10 0 6 0 2z" fill="#f7a441"/></svg>0612 480 517</span>
  </div>
  <div style="margin-left:-40px">Free Shipping on Orders Over €49 | Fast Delivery Across the Netherlands</div>
  <div><span><svg width="10" height="10" viewBox="0 0 10 10"><path d="M2 0l2 2-1 2 3 3 2-1 2 2-2 2C4 10 0 6 0 2z" fill="#f7a441"/></svg>Questions? 085-0102030</span></div>
</div>

<header class="abs header">
  <div class="abs logo">Brenvik</div>
  <div class="abs search">Search our store...<b><svg width="10" height="10" viewBox="0 0 10 10"><circle cx="4" cy="4" r="3" stroke="#fff" stroke-width="1.5" fill="none"/><path d="M6.5 6.5L9 9" stroke="#fff" stroke-width="1.5"/></svg>Search</b></div>
  <div class="abs hbtn" style="left:958px"><svg width="14" height="14" viewBox="0 0 14 14"><circle cx="7" cy="4" r="3" fill="#3c3c3b"/><path d="M1 14c0-4 3-6 6-6s6 2 6 6z" fill="#3c3c3b"/></svg></div>
  <div class="abs hbtn" style="left:1008px"><svg width="15" height="13" viewBox="0 0 15 13"><path d="M7.5 13L1 6.5C-1 4 1 0 4 0c1.6 0 2.8 1 3.5 2C8.2 1 9.4 0 11 0c3 0 5 4 3 6.5z" fill="#3c3c3b"/></svg></div>
  <div class="abs hbtn" style="left:1060px"><svg width="15" height="14" viewBox="0 0 15 14"><path d="M0 1h3l2 8h8l2-6H4" stroke="#3c3c3b" stroke-width="1.6" fill="none"/><circle cx="6" cy="12" r="1.4" fill="#3c3c3b"/><circle cx="12" cy="12" r="1.4" fill="#3c3c3b"/></svg></div>
</header>
<nav class="abs nav">
  <a>Home</a><a>Fish Food</a><a>Chicken Food</a><a>Accessories</a><a>About Us</a><a>Blog</a><a>Contact</a>
</nav>

<section class="abs hero-main">
  <div class="abs hero-photo" role="img" aria-label="Photo of a red-combed chicken on a golden field"></div>
  <h1 class="abs hero-title">Healthy <em>Chickens,</em><br>Happier Farms!</h1>
  <p class="abs hero-sub">High-quality nutrition for better growth and stronger flocks.</p>
  <a class="abs hero-cta">Shop<br>Chicken<br>Food</a>
</section>
<section class="abs hero-side" role="img" aria-label="Photo of a colourful fish swimming among orange water plants">
  <h2>Feed Your<br>Fish the Best —<br>Every Time!</h2>
</section>

<h2 class="abs h-center" style="top:730px">Shop by Category</h2>
<div class="abs cat-tile" style="left:288px;background:#c9e7fb"></div>
<div class="abs cat-tile" style="left:503px;background:#f1f182"></div>
<div class="abs cat-tile" style="left:717px;background:#dedede"></div>
<div class="abs cat-pack" style="left:345px;width:80px;height:160px;background:linear-gradient(180deg,#1d5fb8,#3c8ee0 60%,#1e4f9c)" role="img" aria-label="Fish food pouch"></div>
<div class="abs cat-pack" style="left:557px;width:86px;height:158px;background:linear-gradient(180deg,#e8e0c8,#8a6a44 50%,#d8cfb4)" role="img" aria-label="Chicken feed bag"></div>
<div class="abs cat-pack" style="left:738px;top:808px;width:150px;height:110px;border-radius:50px;background:radial-gradient(ellipse,#3a3a3a 0%,#666 50%,rgba(222,222,222,0) 72%)" role="img" aria-label="Black leash accessory"></div>
<div class="abs cat-label" style="left:288px">Fish Food</div>
<div class="abs cat-label" style="left:503px">Chicken Food</div>
<div class="abs cat-label" style="left:717px">Accessories</div>

<div class="abs divider" style="top:1053px"></div>

<h2 class="abs fav-title">Customer Favorites</h2>
<p class="abs fav-desc" style="width:515px">Discover our most popular, high-quality feed products — trusted by fish keepers, poultry owners, and professionals across the Netherlands.</p>
<div class="abs arrow" style="left:987px;background:var(--dark)"><svg width="10" height="10" viewBox="0 0 10 10"><path d="M6.5 1.5L3 5l3.5 3.5" stroke="#fff" stroke-width="1.6" fill="none"/></svg></div>
<div class="abs arrow" style="left:1042px;background:var(--orange);border:2px solid var(--dark)"><svg width="10" height="10" viewBox="0 0 10 10"><path d="M3.5 1.5L7 5 3.5 8.5" stroke="#fff" stroke-width="1.6" fill="none"/></svg></div>

<div class="abs card" style="left:107px">
  <div class="img"><div class="pack" style="background:linear-gradient(180deg,#e0632a,#2a2a2a 40%,#e0632a)" role="img" aria-label="Goldfish pellets pack"></div></div>
  <div class="stars">★★★★★</div><div class="name">Premium<br>Goldfish Pellets</div>
  <div class="price">€8.99<small>Weight: 1kg</small></div>
  <div class="cart"><svg width="15" height="14" viewBox="0 0 15 14"><path d="M0 1h3l2 8h8l2-6H4z" fill="#fff"/><circle cx="6" cy="12" r="1.4" fill="#fff"/><circle cx="12" cy="12" r="1.4" fill="#fff"/></svg></div>
</div>
<div class="abs card" style="left:357px">
  <div class="img"><div class="pack" style="left:56px;width:100px;background:linear-gradient(180deg,#e9e3d0,#3f4a2e 45%,#d7cdb3)" role="img" aria-label="Two organic layer feed bags"></div></div>
  <div class="stars">★★★★★</div><div class="name">Organic<br>Layer Feed</div>
  <div class="price">€12.50<small>Weight: 5kg</small></div>
  <div class="cart"><svg width="15" height="14" viewBox="0 0 15 14"><path d="M0 1h3l2 8h8l2-6H4z" fill="#fff"/><circle cx="6" cy="12" r="1.4" fill="#fff"/><circle cx="12" cy="12" r="1.4" fill="#fff"/></svg></div>
</div>
<div class="abs card" style="left:607px">
  <div class="img"><div class="pack" style="background:linear-gradient(180deg,#f2f2f2,#6fa34a 55%,#f0f0f0)" role="img" aria-label="Pond mix bag"></div></div>
  <div class="stars">★★★★★</div><div class="name">Pond<br>Mix 5kg</div>
  <div class="price">€24.99<small>Weight: 5kg</small></div>
  <div class="cart"><svg width="15" height="14" viewBox="0 0 15 14"><path d="M0 1h3l2 8h8l2-6H4z" fill="#fff"/><circle cx="6" cy="12" r="1.4" fill="#fff"/><circle cx="12" cy="12" r="1.4" fill="#fff"/></svg></div>
</div>
<div class="abs card" style="left:857px">
  <div class="img"><div class="pack" style="left:70px;width:72px;background:linear-gradient(180deg,#e6c58a,#d98a3a 55%,#e6c58a)" role="img" aria-label="Chick starter crumbs bag"></div></div>
  <div class="stars">★★★★★</div><div class="name">Chick<br>Starter Crumbs</div>
  <div class="price">€9.75<small>Weight: 2kg</small></div>
  <div class="cart"><svg width="15" height="14" viewBox="0 0 15 14"><path d="M0 1h3l2 8h8l2-6H4z" fill="#fff"/><circle cx="6" cy="12" r="1.4" fill="#fff"/><circle cx="12" cy="12" r="1.4" fill="#fff"/></svg></div>
</div>

<div class="abs promo">
  <p>$35 Off ! Your first repeat delivery order of $95</p>
  <a>Shop now</a>
  <i><svg width="8" height="8" viewBox="0 0 8 8"><path d="M2.5 1L5.5 4 2.5 7" stroke="#3c3c3b" stroke-width="1.4" fill="none"/></svg></i>
</div>

<div class="abs divider" style="top:1682px"></div>

<h2 class="abs deals-title">This Week’s Special Deals</h2>
<a class="abs pill" style="left:943px;top:1752px;width:143px">Shop Offers</a>

<div class="abs deal" style="left:113px;top:1820px;width:442px;height:175px;background:linear-gradient(100deg,#f29a1e 0%,#e98a1c 45%,#a9581f 75%,#c97a34 100%)" role="img" aria-label="Photo of chickens feeding on a farm">
  <h3 style="left:46px;top:45px">Buy 2 Get<br>1 Free – Chicken<br>Feed Range!</h3>
</div>
<div class="abs deal" style="left:113px;top:2013px;width:442px;height:174px;background:linear-gradient(100deg,#2f4a12 0%,#3b5a16 45%,#6a3a1a 75%,#d86a2a 90%,#304a18 100%)" role="img" aria-label="Photo of a koi fish in a pond">
  <h3 style="left:47px;top:57px">10% Off All<br>Pond Food – Limited<br>Time Only!</h3>
</div>
<div class="abs deal" style="left:575px;top:1820px;width:510px;height:367px;background:linear-gradient(100deg,#6f9c2c 0%,#86ad3e 40%,#b08a5e 70%,#7a5a3a 100%)" role="img" aria-label="Photo of a smiling farmer holding a chicken">
  <svg class="abs" style="left:55px;top:80px" width="92" height="58" viewBox="0 0 92 58"><path d="M0 4h54v38H0z M58 16h18l14 16v10H58z" fill="#fff"/><circle cx="20" cy="46" r="10" fill="#fff" stroke="#86ad3e" stroke-width="4"/><circle cx="72" cy="46" r="10" fill="#fff" stroke="#86ad3e" stroke-width="4"/></svg>
  <h3 style="left:55px;top:162px;font-size:25px;line-height:32px">Free Shipping<br>on Orders Above</h3>
  <h3 style="left:54px;top:238px;font-size:56px;line-height:60px">€49!</h3>
</div>

<div class="abs feat" style="left:147px">
  <div class="ic" style="background:var(--orange)"><svg width="30" height="20" viewBox="0 0 30 20"><path d="M0 2h17v12H0z M19 6h6l5 5v3H19z" fill="#fff"/><circle cx="7" cy="16" r="3" fill="#fff" stroke="#f7a441" stroke-width="1.5"/><circle cx="24" cy="16" r="3" fill="#fff" stroke="#f7a441" stroke-width="1.5"/></svg></div>
  <div><b>Fast Delivery</b><small>Across the Netherlands</small></div>
</div>
<div class="abs feat" style="left:447px">
  <div class="ic" style="background:var(--dark)"><svg width="26" height="26" viewBox="0 0 26 26"><circle cx="13" cy="13" r="10" fill="none" stroke="#fff" stroke-width="2"/><path d="M8 13l3.5 3.5L18 10" stroke="#fff" stroke-width="2.2" fill="none"/></svg></div>
  <div><b>High-Quality Nutrition</b><small>For Fish &amp; Poultry</small></div>
</div>
<div class="abs feat" style="left:812px">
  <div class="ic" style="background:#e3e3e3"><svg width="28" height="22" viewBox="0 0 28 22"><rect x="1" y="3" width="22" height="17" rx="3" fill="#3c3c3b"/><rect x="15" y="8" width="12" height="7" rx="2" fill="#e3e3e3" stroke="#3c3c3b" stroke-width="1.5"/></svg></div>
  <div><b>Secure Payments</b><small>Shop with Confidence</small></div>
</div>

<div class="abs divider" style="top:2390px"></div>

<h2 class="abs h-center" style="top:2455px">Why Choose Brenvik.nl?</h2>

<div class="abs why" style="left:146px">
  <div class="circle"><svg width="40" height="40" viewBox="0 0 40 40"><path d="M20 5l4.5 10 11 1-8.5 7.5 2.5 11L20 29l-9.5 5.5 2.5-11L4.5 16l11-1z" fill="none" stroke="#fff" stroke-width="3" stroke-linejoin="round"/></svg></div>
  <p>Over 25 years of experience in animal nutrition</p>
</div>
<div class="abs why" style="left:334px">
  <div class="circle"><svg width="40" height="36" viewBox="0 0 40 36"><path d="M20 34L5 19C-2 12 4 0 13 2c3 1 5 3 7 6 2-3 4-5 7-6 9-2 15 10 8 17z" fill="#fff"/></svg></div>
  <p>Trusted by farms, breeders, and hobbyists</p>
</div>
<div class="abs why" style="left:525px">
  <div class="circle"><svg width="40" height="40" viewBox="0 0 40 40"><path d="M6 36C4 16 16 4 36 4c0 22-12 32-30 32z" fill="#fff"/><path d="M6 36L26 14" stroke="#f7a441" stroke-width="2.5"/></svg></div>
  <p>Carefully selected, premium-quality ingredients</p>
</div>
<div class="abs why" style="left:707px">
  <div class="circle"><svg width="46" height="32" viewBox="0 0 46 32"><path d="M0 2h27v20H0z M30 8h9l7 8v6H30z" fill="#fff"/><circle cx="9" cy="26" r="5" fill="#fff" stroke="#f7a441" stroke-width="2"/><circle cx="37" cy="26" r="5" fill="#fff" stroke="#f7a441" stroke-width="2"/></svg></div>
  <p>Fast and reliable nationwide delivery</p>
</div>
<div class="abs why" style="left:895px">
  <div class="circle"><svg width="42" height="42" viewBox="0 0 42 42"><circle cx="21" cy="19" r="17" fill="#fff"/><path d="M10 31l-4 9 11-5z" fill="#fff"/><circle cx="14" cy="19" r="2.4" fill="#f7a441"/><circle cx="21" cy="19" r="2.4" fill="#f7a441"/><circle cx="28" cy="19" r="2.4" fill="#f7a441"/></svg></div>
  <p>Excellent customer support</p>
</div>

<div class="abs partner-img" role="img" aria-label="Photo of a farmer crouching to feed a rooster beside a red barn"></div>
<section class="partner">
  <h2 class="abs">Your Partner in<br>Quality Animal Feed</h2>
  <p class="abs">Lorem ipsum dolor sit amet, consectetur adipiscing elit. Proin vel magna a nisl fermentum consectetur. Sed vehicula orci at lectus tincidunt, vel tincidunt ex posuere. Curabitur aliquet, urna vel iaculis pretium, justo mauris tempor justo, vitae pretium ipsum neque ut urna. Pellentesque habitant morbi tristique senectus et netus et malesuada fames ac turpis egestas.</p>
  <a class="abs pill" style="left:635px;top:3177px;width:144px">Shop Offers</a>
</section>

<footer class="abs footer">
  <div class="abs fcol" style="left:107px"><h4>Customer Service</h4><ul><li>Shipping &amp; Delivery</li><li>Returns &amp; Refunds</li><li>Payment Options</li><li>Contact Us</li></ul></div>
  <div class="abs fsep" style="left:330px"></div>
  <div class="abs fcol" style="left:384px"><h4>About Brenvik.nl</h4><ul><li>Our Story</li><li>Sustainability</li><li>Careers</li><li>Blog</li></ul></div>
  <div class="abs fsep" style="left:585px"></div>
  <div class="abs fcol" style="left:641px"><h4>My Account</h4><ul><li>Login / Register</li><li>Order History</li><li>Wishlist</li></ul></div>
  <div class="abs fsep" style="left:830px"></div>
  <div class="abs fcol contact" style="left:882px"><h4>Stay Connected</h4><ul>
    <li><svg width="12" height="14" viewBox="0 0 12 14"><path d="M6 0a5 5 0 015 5c0 4-5 9-5 9S1 9 1 5a5 5 0 015-5z" fill="#f7a441"/><circle cx="6" cy="5" r="2" fill="#3c3c3b"/></svg><span>Brenvik B.V., Amsterdam,<br>The Netherlands</span></li>
    <li><svg width="13" height="10" viewBox="0 0 13 10" style="margin-top:3px"><rect width="13" height="10" rx="1" fill="#f7a441"/><path d="M0 1l6.5 5L13 1" stroke="#3c3c3b" fill="none"/></svg>info@brenvik.nl</li>
    <li><svg width="13" height="13" viewBox="0 0 10 10" style="margin-top:2px"><path d="M2 0l2 2-1 2 3 3 2-1 2 2-2 2C4 10 0 6 0 2z" fill="#f7a441"/></svg>+31 20 555 0148</li>
  </ul></div>
  <div class="abs totop"><svg width="10" height="10" viewBox="0 0 10 10"><path d="M2 6.5L5 3.5 8 6.5" stroke="#fff" stroke-width="1.5" fill="none"/></svg></div>
  <div class="abs social" style="left:129px"></div>
  <div class="abs social" style="left:171px"></div>
  <div class="abs social" style="left:211px"></div>
  <div class="abs fbottom" style="left:0;width:1200px;text-align:center">© 2025 Brenvik.nl — All Rights Reserved</div>
  <div class="abs fbottom" style="left:901px">Terms &amp; Conditions | Privacy Policy</div>
</footer>

</body>
</html>
```